Brightwell Audiology Centre - is state of the art audiology clinic and needs a business card design

the card should be oriented in 'portrait' mode and have a clinic logo. The card should be double sided, with logo on the front and my details on the other side of the card

We would also like to use a tagline of 'Experts in Hearing Care'

Clinic

```html
<!DOCTYPE html>
<html lang="en">
<head>
<meta charset="utf-8">
<title>Brightwell Audiology Centre – Business Card</title>
<link href="https://fonts.googleapis.com/css2?family=Lato:ital,wght@0,400;0,700;0,900;1,400&display=swap" rel="stylesheet">
<style>
  :root {
    --stage: #2e2e2e;
    --card: #f7f7f7;
    --card-edge: #e4e4e4;
    --brand-blue: #5fb0e6;
    --deep-blue: #2a7fc4;
    --ink-grey: #6e6e6e;
    --text-dark: #3a3a3a;
  }
  * { margin: 0; padding: 0; box-sizing: border-box; }
  html, body {
    width: 1200px; height: 900px; overflow: hidden;
    background: var(--stage);
    font-family: "Lato", sans-serif;
  }
  .stage {
    position: relative; width: 1200px; height: 900px;
    display: flex; align-items: center; justify-content: center; gap: 70px;
  }
  .card {
    background: linear-gradient(160deg, #ffffff 0%, var(--card) 60%, var(--card-edge) 100%);
    box-shadow: 0 18px 40px rgba(0,0,0,.5);
    position: relative;
  }
  /* Front */
  .card-front {
    width: 340px; height: 560px;
    display: flex; flex-direction: column; align-items: center; justify-content: center;
    text-align: center;
  }
  .brand-mark {
    width: 70px; height: 70px; border-radius: 50%;
    background: var(--brand-blue); margin-bottom: 34px;
  }
  .brand-name {
    color: var(--ink-grey); font-weight: 700;
    font-size: 40px; line-height: 1.05; letter-spacing: 2px; text-transform: uppercase;
  }
  .tagline {
    margin-top: 46px; color: var(--brand-blue);
    font-size: 15px; letter-spacing: 3px; text-transform: uppercase;
  }
  /* Back */
  .card-back { width: 340px; height: 560px; padding: 34px 30px; }
  .person { text-align: center; }
  .person-name {
    color: var(--brand-blue); font-weight: 900; font-size: 22px; letter-spacing: .5px;
    text-transform: uppercase;
  }
  .person-degrees { color: var(--ink-grey); font-weight: 700; font-size: 13px; margin-top: 3px; }
  .person-role { color: var(--ink-grey); font-size: 13px; line-height: 1.25; }
  .back-brand {
    display: flex; align-items: center; gap: 18px; margin: 40px 0 46px 6px;
  }
  .back-brand .brand-mark { width: 54px; height: 54px; margin: 0; flex: none; }
  .back-brand .brand-name { font-size: 25px; text-align: left; }
  .contact-list { list-style: none; }
  .contact-list li {
    display: flex; align-items: center; gap: 16px;
    color: var(--text-dark); font-size: 14px; height: 38px;
  }
  .contact-list .address { align-items: flex-start; height: auto; line-height: 1.9; }
  .contact-icon { width: 26px; height: 26px; flex: none; fill: none; stroke: var(--brand-blue); stroke-width: 2; }
  .contact-icon .solid { fill: var(--brand-blue); stroke: none; }
</style>
</head>
<body>
<main class="stage">

  <section class="card card-front" aria-label="Card front">
    <div class="brand-mark" aria-hidden="true"></div>
    <h1 class="brand-name">Brightwell<br>Audiology<br>Centre</h1>
    <p class="tagline">Experts in Hearing Care</p>
  </section>

  <section class="card card-back" aria-label="Card back">
    <header class="person">
      <h2 class="person-name">Dr Arjun Mehta</h2>
      <p class="person-degrees">AuD. MASLP. MAudSA.CCP</p>
      <p class="person-role">Chief Audiologist &amp;<br>Speech Language Pathologist</p>
    </header>

    <div class="back-brand">
      <div class="brand-mark" aria-hidden="true"></div>
      <p class="brand-name">Brightwell<br>Audiology<br>Centre</p>
    </div>

    <ul class="contact-list">
      <li>
        <svg class="contact-icon" viewBox="0 0 26 26" aria-hidden="true">
          <path class="solid" d="M3 9c0-3 4-5 10-5s10 2 10 5v2h-5V9h-10v2H3z"/>
          <rect class="solid" x="6" y="12" width="14" height="10" rx="2"/>
        </svg>
        0836 2457810
      </li>
      <li>
        <svg class="contact-icon" viewBox="0 0 26 26" aria-hidden="true">
          <rect x="7" y="2" width="12" height="22" rx="2"/>
          <line x1="11" y1="20" x2="15" y2="20"/>
        </svg>
        9845017263
      </li>
      <li>
        <svg class="contact-icon" viewBox="0 0 26 26" aria-hidden="true">
          <rect x="2" y="6" width="22" height="14" rx="1"/>
          <polyline points="2,6 13,14 24,6"/>
        </svg>
        arjunmehta@mail.com
      </li>
      <li>
        <svg class="contact-icon" viewBox="0 0 26 26" aria-hidden="true">
          <circle cx="13" cy="13" r="10"/>
          <ellipse cx="13" cy="13" rx="4" ry="10"/>
          <line x1="3" y1="13" x2="23" y2="13"/>
        </svg>
        www.brightwellaudiology.in
      </li>
      <li class="address">
        <svg class="contact-icon" viewBox="0 0 26 26" aria-hidden="true">
          <path class="solid" d="M13 2a8 8 0 0 0-8 8c0 6 8 14 8 14s8-8 8-14a8 8 0 0 0-8-8zm0 11a3 3 0 1 1 0-6 3 3 0 0 1 0 6z"/>
        </svg>
        <span>F 4 Lakshmi Arcade, Keshwapur,<br>Hubli - 580 023. (Karnataka)</span>
      </li>
    </ul>
  </section>

</main>
</body>
</html>
```